Business Cards & Stationary for Broadcast Company

We are a satellite company launching a new exciting brand by the name of "Veloran". Veloran is a broadcasting solution provider that gives end-to-end solutions to TV channels and other content providers to deliver and distribute their content globally. Weather it be TV channels that need to be broadcasted in their local regions or internationally, or its collection of news from various locations, or even coverage of special sports or other events, we provide the technology and services to make that happen.
we need a design for business cards as our top priority but also require letterhead and envelope design as well.
Business card will include the following information
Name: Karim Dusoki
Designation: General Manager
Mobile (M): +92 333 4718206
+971 55 2486153 (UAE)
Direct (D): +92 213 6140392
Office (O): +92 213 6142510-14
Fax (F): +92 213 6140392
Email (E): karim@veloran-example.biz
Website: www.veloran-example.biz

```html
<!DOCTYPE html>
<html lang="en">
<head>
<meta charset="utf-8">
<title>Veloran Letterhead</title>
<link href="https://fonts.googleapis.com/css2?family=Tinos:ital,wght@0,400;0,700;1,400&family=Open+Sans:wght@400;600;700&display=swap" rel="stylesheet">
<style>
  :root {
    --backdrop: #e4e4e4;
    --paper: #ffffff;
    --ink: #1c1c1c;
    --muted: #555a60;
    --separator: #aaaaaa;
    --signature-fill: #f2f2f2;
    --navy: #1b4f9c;
    --cyan: #1aa3df;
    --green: #9cc63b;
    --red: #e0252b;
  }
  * { box-sizing: border-box; margin: 0; padding: 0; }
  html, body { width: 1200px; height: 909px; overflow: hidden; }
  body {
    background: var(--backdrop);
    display: flex;
    align-items: center;
    justify-content: center;
  }
  .letterhead {
    position: relative;
    width: 600px;
    height: 849px;
    background: var(--paper);
    box-shadow: 0 4px 18px rgba(0,0,0,0.12);
    overflow: hidden;
  }
  .brand {
    position: absolute;
    top: 42px;
    left: 0;
    right: 0;
    display: flex;
    align-items: center;
    justify-content: center;
    gap: 8px;
  }
  .brand-dot {
    width: 14px;
    height: 14px;
    border-radius: 50%;
    background: var(--navy);
  }
  .brand-name {
    font-family: "Open Sans", sans-serif;
    font-weight: 700;
    font-size: 20px;
    letter-spacing: 2px;
    color: var(--navy);
    text-transform: uppercase;
  }
  .letter {
    position: absolute;
    top: 210px;
    left: 64px;
    right: 64px;
    font-family: "Tinos", serif;
    font-size: 12px;
    line-height: 1.3;
    color: var(--ink);
  }
  .letter p { text-align: justify; margin-bottom: 14px; }
  .letter .salutation { margin-bottom: 12px; }
  .closing { margin-top: 40px; }
  .closing p { margin-bottom: 0; text-align: left; }
  .signature-mark {
    display: block;
    width: 110px;
    height: 34px;
    margin: 6px 0 2px;
  }
  .contact-strip {
    position: absolute;
    left: 30px;
    right: 30px;
    bottom: 24px;
    font-family: "Open Sans", sans-serif;
    font-size: 6.6px;
    color: var(--muted);
    display: flex;
    justify-content: space-between;
    white-space: nowrap;
  }
  .contact-strip b { color: var(--ink); font-weight: 700; margin-right: 2px; }
  .contact-strip .web { font-weight: 700; color: var(--ink); }
  .contact-strip .sep { color: var(--separator); }
  .color-bars {
    position: absolute;
    left: 0;
    right: 0;
    bottom: 0;
    height: 6px;
    display: flex;
  }
  .color-bars span { flex: 1; }
  .bar-navy { background: var(--navy); }
  .bar-cyan { background: var(--cyan); }
  .bar-green { background: var(--green); }
  .bar-red { background: var(--red); }
</style>
</head>
<body>
  <main class="letterhead">
    <header class="brand">
      <span class="brand-dot"></span>
      <span class="brand-name">Veloran</span>
    </header>

    <article class="letter">
      <p class="salutation">Gentlemen,</p>
      <p>Enclosed I have the honor to send you an article which I should be pleased if you would accept for the “Meridian Review”. I am <i>desperately</i> pushed for money; and in the event of Mr. Halloran’s liking the “Landscape-Garden” I would take it as an especial favor if you would mail me the amount due for it, so as to reach me here by the 21st, on which day I shall need it. Can you possibly oblige me in this? If you accept the paper I presume you will allow me your usual sum, whatever that is for similar contributions—but I set no price—leaving all to your own liberality. The piece will make 8 of your pages and rather more.</p>
      <p>Will you be kind enough to put the best possible interpretation upon my behavior while in N-York? You must have conceived a <i>queer</i> idea of me—but the simple truth is that Whitcombe would insist upon <i>the juleps</i>, and I knew not what I was either doing or saying. The Review of Danvers which I offered you was deficient in a 1/2 page of commencement, which I had written to supersede the old beginning, and which gave the article the character of a general and retrospective review. No wonder you did not take it—I would have been very much mortified if you had. I hope to see you at some future time, under better auspices.</p>
      <div class="closing">
        <p>In the meantime I remain</p>
        <p>Yours very truly,</p>
        <svg class="signature-mark" role="img" aria-label="Handwritten signature of Elias Marlowe" viewBox="0 0 110 34">
          <rect width="110" height="34" fill="var(--signature-fill)"/>
        </svg>
        <p>Elias Marlowe</p>
      </div>
    </article>

    <footer class="contact-strip">
      <span><b>M</b>+92 333 4718206</span><span class="sep">|</span>
      <span>+971 55 2486153 (UAE)</span><span class="sep">|</span>
      <span><b>D</b>+92 213 6140392</span><span class="sep">|</span>
      <span class="web">www.veloran-example.biz</span><span class="sep">|</span>
      <span><b>O</b>+92 213 6142510-14</span><span class="sep">|</span>
      <span><b>F</b>+92 213 6140392</span><span class="sep">|</span>
      <span><b>E</b>karim@veloran-example.biz</span>
    </footer>

    <div class="color-bars">
      <span class="bar-navy"></span>
      <span class="bar-cyan"></span>
      <span class="bar-green"></span>
      <span class="bar-red"></span>
    </div>
  </main>
</body>
</html>
```